Präsentationsvorlagen/Workbook für Coaching - Yoga - Training
Zielgruppe
Coaching - Yoga - Training, d.h. Yogaunterricht, Einzelcoaching, Seminare und Workshops rund um das Thema Stress/Resilienz/Achtsamkeit
Zielgruppe sind einerseits überwiegend Frauen, aber auch Firmenkunden, die für ihre Mitarbeiter Seminare und Yoga anbieten.
Aufgabenstellung
Ich benötige einen professionellen ppt Auftritt für Präsentationen/Workbooks mit meinen Firmenfarben (grau, weiß, rosa, beige) in den mein Logo integriert ist.
Das Design sollte dem Thema entsprechend 'warm' sein aber die nötige Professionalität für Firmenkunden ausstrahlen.

```html
<!DOCTYPE html>
<html lang="de">
<head>
<meta charset="utf-8">
<title>Lena Marwick – Präsentationsvorlagen</title>
<link href="https://fonts.googleapis.com/css2?family=Cinzel:wght@400;600&family=Open+Sans:wght@400&display=swap" rel="stylesheet">
<style>
  :root{
    --stage:#e7e5e7;
    --rose:#b0457b;
    --rose-deep:#9c3a6c;
    --beige:#d8a985;
    --cream:#f4f0ea;
    --white:#fbfafa;
    --ink:#4a3f44;
    --grey:#6b6266;
    --heading:'Cinzel', serif;
    --body:'Open Sans', sans-serif;
  }
  *{box-sizing:border-box;margin:0;padding:0}
  html,body{width:1200px;height:622px;overflow:hidden;background:var(--stage)}
  .canvas{position:relative;width:1200px;height:622px;background:radial-gradient(ellipse at 50% 40%,#f1f0f1 0%,var(--stage) 70%)}
  .slide{position:absolute;overflow:hidden;box-shadow:0 6px 18px rgba(90,70,80,.12)}
  .slide svg.bg{position:absolute;inset:0;width:100%;height:100%}
  .h{font-family:var(--heading);font-weight:600;letter-spacing:.03em;line-height:1.1}
  .sub{font-family:var(--heading);font-size:7px;letter-spacing:.03em;line-height:1.25}
  .copy{font-family:var(--body);font-size:3.6px;line-height:1.45}
  .brand-mini{position:absolute;display:flex;align-items:center;gap:2px;font-family:var(--heading);font-size:4px;color:var(--rose)}
  .brand-mini i{display:block;width:9px;height:9px;border-radius:50%;border:1px solid var(--rose)}
  .photo{position:absolute}
  .round{border-radius:50%}
  .abs{position:absolute}

  /* Kursübersicht */
  .s-courses{left:276px;top:67px;width:294px;height:164px;background:var(--white)}
  .s-courses .photo{left:0;top:0;width:98px;height:164px;background:linear-gradient(180deg,#ead9e2 0%,#f1e2e3 45%,#e8cdd2 60%,#f3e7ea 100%)}
  .s-courses .h{left:123px;top:31px;font-size:10px;color:var(--rose)}
  .col{position:absolute;top:57px;width:56px;text-align:center}
  .col .dot{width:38px;height:38px;border-radius:50%;margin:0 auto 7px}
  .col .lbl{font-family:var(--heading);font-size:5.5px;color:var(--rose);margin-bottom:3px}
  .col .copy{color:var(--grey)}

  /* Angebote */
  .s-offers{left:610px;top:67px;width:296px;height:164px;background:var(--white)}
  .disc{position:absolute;border-radius:50%;text-align:center;color:#fff}
  .disc .h{font-size:10px;color:#fff}
  .disc .sub{font-size:5.5px;color:#fff;margin-top:4px}

  /* Training */
  .s-training{left:90px;top:198px;width:303px;height:171px;background:var(--cream)}
  .s-training .h{left:21px;top:30px;font-size:12px;color:var(--rose)}
  .s-training .sub{left:21px;top:48px;color:var(--rose)}
  .s-training .copy{left:18px;top:66px;width:130px;color:var(--rose-deep)}

  /* Yoga */
  .s-yoga{left:801px;top:198px;width:309px;height:169px;background:var(--white)}
  .s-yoga .h{left:126px;top:37px;font-size:12px;color:#fff}
  .s-yoga .sub{left:126px;top:54px;color:#fff}
  .s-yoga .copy{left:126px;top:80px;width:150px;color:#fff}

  /* Coaching */
  .s-coaching{left:172px;top:315px;width:319px;height:179px;background:var(--beige)}
  .s-coaching .photo{left:0;top:0;width:58px;height:179px;background:linear-gradient(180deg,#6e6aa5 0%,#b58aa6 35%,#e3b6a4 50%,#8a6f93 70%,#2f2a4a 100%)}
  .s-coaching .h{left:82px;top:40px;font-size:12px;color:#fff}
  .s-coaching .sub{left:82px;top:58px;color:#fff}
  .s-coaching .copy{left:82px;top:82px;width:160px;color:#fff}

  /* Titelfolie mit Foto */
  .s-cover{left:426px;top:256px;width:341px;height:203px;background:linear-gradient(180deg,#ecc9b1 0%,#f2d3bd 45%,#e9c0a4 62%,#d9ac8e 100%)}

  /* Titelfolie mit Namen */
  .s-title{left:705px;top:315px;width:318px;height:179px;background:var(--cream)}
  .s-title .wordmark{position:absolute;left:0;right:0;top:72px;text-align:center}
  .s-title .wordmark .ring{display:block;width:22px;height:22px;border-radius:50%;border:1.5px solid var(--rose);margin:0 auto 8px}
  .s-title .name{font-family:var(--heading);font-size:16px;color:var(--ink);letter-spacing:.04em}
  .s-title .tag{font-family:var(--heading);font-size:6.5px;color:var(--rose);letter-spacing:.05em;margin-top:2px}
</style>
</head>
<body>
<main class="canvas">

  <!-- Kursübersicht -->
  <section class="slide s-courses">
    <div class="photo" role="img" aria-label="Ruhige Seelandschaft im zarten Morgenlicht"></div>
    <h2 class="h abs">Yoga Kurse</h2>
    <div class="brand-mini" style="right:10px;top:10px"><i></i></div>
    <div class="col" style="left:118px">
      <div class="dot" style="background:var(--rose)" role="img" aria-label="Symbol: meditierende Person"></div>
      <div class="lbl">Termine</div>
      <p class="copy">jeden Montag<br>ab 19 Uhr<br>jeden Freitag<br>ab 20 Uhr</p>
    </div>
    <div class="col" style="left:176px">
      <div class="dot" style="background:#f1e4ea" role="img" aria-label="Symbol: Yogahaltung im Stand"></div>
      <div class="lbl">Inhalte</div>
      <p class="copy">Hatha Yoga<br>Asanas<br>körperliche Übungen<br>Pranayama<br>Atemübungen<br>Meditation</p>
    </div>
    <div class="col" style="left:234px">
      <div class="dot" style="background:var(--beige)" role="img" aria-label="Symbol: Yogahaltung im Ausfallschritt"></div>
      <div class="lbl">Ziele</div>
      <p class="copy">zur Ruhe kommen<br>Spannungen lösen</p>
    </div>
  </section>

  <!-- Angebote -->
  <section class="slide s-offers">
    <svg class="bg" viewBox="0 0 296 164" preserveAspectRatio="none" aria-hidden="true">
      <path d="M0 150 Q150 125 296 138 L296 164 L0 164Z" fill="#efe3e8"/>
    </svg>
    <div class="brand-mini" style="right:10px;top:10px"><i></i></div>
    <div class="disc" style="left:24px;top:36px;width:118px;height:118px;background:var(--beige)">
      <div class="h" style="margin-top:48px">Yoga Kurse</div>
      <div class="sub">_ Innere Ruhe und<br>Steigerung des Wohl-<br>befindens</div>
    </div>
    <div class="photo round" style="left:50px;top:12px;width:64px;height:64px;border:3px solid #fff;background:linear-gradient(180deg,#6b5b70 0%,#e59a6a 45%,#f6c98e 55%,#3b3340 100%)" role="img" aria-label="Boot am See bei Sonnenaufgang"></div>
    <div class="disc" style="left:155px;top:36px;width:118px;height:118px;background:var(--rose)">
      <div class="h" style="margin-top:48px">Nordic<br>Walking</div>
      <div class="sub">_ Körper und Geist<br>im Einklang mit<br>der Natur</div>
    </div>
    <div class="photo round" style="left:182px;top:12px;width:64px;height:64px;border:3px solid #fff;background:linear-gradient(180deg,#e9e2ec 0%,#d9cbe0 60%,#2a2428 78%,#2a2428 100%)" role="img" aria-label="Yogaübung im Gegenlicht auf einem Felsen"></div>
  </section>

  <!-- Training -->
  <section class="slide s-training">
    <svg class="bg" viewBox="0 0 303 171" preserveAspectRatio="none" aria-hidden="true">
      <path d="M230 171 Q250 120 303 110 L303 171Z" fill="#fbf9f6"/>
    </svg>
    <div class="brand-mini" style="right:14px;top:14px"><i></i></div>
    <h2 class="h abs">Training</h2>
    <p class="sub abs">_ Mit Freude Neues erlernen!</p>
    <p class="copy abs">Als zertifizierte Trainerin in der Erwachsenenbildung begleite ich Menschen dabei, sich weiterzuentwickeln. In zahlreichen Fachtrainings durfte ich meine Erfahrung einbringen. Mein Ansatz ist professionell und didaktisch durchdacht, mit Inhalten, die individuell auf Ihre Zielgruppe abgestimmt sind. Suchen Sie eine kompetente Partnerin für Trainings Ihrer Mitarbeiter? Sprechen Sie mich gerne an!</p>
    <div class="photo round" style="left:170px;top:12px;width:88px;height:88px;background:linear-gradient(180deg,#5d4c5a 0%,#d98a5e 42%,#f7c27e 52%,#6a4d4d 70%,#1f1a22 100%)" role="img" aria-label="Boot am nebligen See bei Sonnenaufgang"></div>
  </section>

  <!-- Yoga -->
  <section class="slide s-yoga">
    <svg class="bg" viewBox="0 0 309 169" preserveAspectRatio="none" aria-hidden="true">
      <path d="M0 169 L0 110 Q60 95 100 40 Q130 0 170 0 L309 0 L309 169Z" fill="var(--beige)"/>
    </svg>
    <div class="brand-mini" style="right:12px;top:12px"><i style="border-color:#fff"></i></div>
    <div class="photo round" style="left:9px;top:12px;width:86px;height:86px;background:linear-gradient(180deg,#e9dfeb 0%,#d6c5db 62%,#2a2428 74%,#2a2428 100%)" role="img" aria-label="Yogaübung im Gegenlicht auf einem Felsen"></div>
    <h2 class="h abs">Yoga</h2>
    <p class="sub abs">_ Innere Ruhe und Steigerung<br>des Wohlbefindens</p>
    <p class="copy abs">Yoga ist das Zur-Ruhe-Kommen der Gedanken. Seit Jahrtausenden ist diese Philosophie eine Kraftquelle, um Spannungen auf körperlicher und seelischer Ebene zu lösen. Ich unterrichte Hatha Yoga mit Asanas, Atemübungen und Meditation, für Anfänger und Fortgeschrittene gleichermaßen.</p>
  </section>

  <!-- Coaching -->
  <section class="slide s-coaching">
    <div class="photo" role="img" aria-label="See in der Abenddämmerung mit Bergsilhouette"></div>
    <svg class="bg" viewBox="0 0 319 179" preserveAspectRatio="none" aria-hidden="true">
      <path d="M40 0 Q80 40 50 100 Q35 150 60 179 L0 179 L0 0Z" fill="none"/>
      <path d="M270 179 Q285 120 319 100 L319 179Z" fill="#2f2a4a"/>
    </svg>
    <h2 class="h abs">Coaching</h2>
    <p class="sub abs">_ Zurück zur Selbstfürsorge<br>und Selbstbestimmtheit</p>
    <p class="copy abs">Wo stehst Du heute? Und wo möchtest Du hin? Coaching ist ein lösungsorientierter Prozess, der Dir in herausfordernden Lebenssituationen dabei hilft, Deine Situation aus verschiedenen Blickwinkeln zu betrachten. Gemeinsam entdecken wir Deine Ressourcen und aktivieren sie. In einem sicheren und vertrauensvollen Rahmen begleite ich Dich auf Deinem Weg.</p>
  </section>

  <!-- Titelfolie mit Foto -->
  <section class="slide s-cover" role="img" aria-label="Yogaübung am Strand im warmen Abendlicht"></section>

  <!-- Titelfolie mit Namen -->
  <section class="slide s-title">
    <svg class="bg" viewBox="0 0 318 179" preserveAspectRatio="none" aria-hidden="true">
      <path d="M0 0 L180 0 Q120 10 70 22 Q30 30 0 28Z" fill="var(--beige)"/>
      <path d="M0 165 Q120 130 220 145 Q280 150 318 135 L318 179 L0 179Z" fill="var(--beige)"/>
    </svg>
    <div class="brand-mini" style="right:14px;top:14px"><i></i></div>
    <div class="wordmark">
      <span class="ring" aria-hidden="true"></span>
      <div class="name">Lena Marwick</div>
      <div class="tag">Coaching - Yoga - Training</div>
    </div>
  </section>

</main>
</body>
</html>
```